I own a rendering company which is in the construction industry i already have a logo i would like i

I want to make the website look professional and blends nicely with the logo, if i can have contact information and photos logos and a place where they can email me for job quotes or request and we want to win the big jobs so think also corporate in conjunction with construction. also an area for brief description and about us

Target Market(s)

Home owners/Investors, Small and major construction companies

Industry/Entity Type

Construction Company

Font styles to use
Serif
Sans Serif

Colors

Designer to choose colors to be used in the design.

Requirements
Must have
• An area for pictures to show with fade changes or clicking options(of white set walls, acrylic render expensive houses walls) an "about us" section. An area to where potential customers can email us (a writing box) where we can receive request for quotes and potential jobs. all contact information and license numbers
Nice to have
• pictures of plastered walls (posh elegant) and rendered walls acrylic and cement render
Should not have
• anything boring plain font etc

```html
<!DOCTYPE html>
<html lang="en">
<head>
<meta charset="utf-8">
<title>Kestrel Rendering</title>
<link href="https://fonts.googleapis.com/css2?family=Raleway:wght@300;400;600;700&family=Open+Sans:ital,wght@0,400;0,600;0,700;1,400;1,600&display=swap" rel="stylesheet">
<style>
:root{
  --red:#e5202a;
  --red-deep:#d41820;
  --ink:#262626;
  --text:#555;
  --light:#f4f4f4;
  --white:#fff;
  --black:#000;
}
*{box-sizing:border-box;margin:0;padding:0}
html,body{width:1200px;height:2773px;overflow:hidden}
body{position:relative;background:var(--white);font-family:"Open Sans",Arial,sans-serif;color:var(--text)}
.abs{position:absolute}
.heading{font-family:"Raleway",Arial,sans-serif;font-weight:700;color:var(--ink);text-transform:uppercase}
.body-copy{font-size:10.5px;line-height:22px;color:#555}
.btn{position:absolute;background:var(--red);color:var(--white);font-family:"Raleway",sans-serif;font-weight:700;font-size:11px;text-transform:uppercase;display:flex;align-items:center;justify-content:center}

/* header */
.top-rule{left:0;top:0;width:1200px;height:5px;background:var(--red)}
.header{left:0;top:5px;width:1200px;height:91px;background:var(--white)}
.brand{left:161px;top:22px;display:flex;align-items:center;gap:10px}
.brand-dot{width:34px;height:34px;border-radius:50%;background:var(--red)}
.brand-name{font-family:"Raleway",sans-serif;font-weight:700;font-size:17px;line-height:18px;color:var(--red);text-transform:uppercase}
.call{left:835px;top:16px;display:flex;align-items:center;gap:10px;font-family:"Open Sans",sans-serif;font-weight:700;font-size:17px;color:var(--red)}
.nav{top:61px;font-family:"Raleway",sans-serif;font-weight:700;font-size:11.5px;color:#222;text-transform:uppercase}
.nav.active{color:var(--red)}

/* hero */
.hero{left:0;top:96px;width:1200px;height:536px;background:linear-gradient(100deg,#b9bcc0 0%,#dfe1e3 28%,#eceef0 55%,#d2d5d8 100%)}
.hero-title{left:161px;top:222px;font-family:"Raleway",sans-serif;font-weight:700;font-size:37px;line-height:46px;text-transform:uppercase}
.hero-title .first{color:var(--red)}
.hero-title .second{color:var(--ink)}
.slide-arrow{width:32px;height:32px;border-radius:50%;border:1.5px solid rgba(255,255,255,.9);display:flex;align-items:center;justify-content:center}
.quick-form{left:716px;top:198px;width:321px;height:333px;background:var(--red);border-radius:3px;padding:18px 18px}
.quick-form h2{font-family:"Raleway",sans-serif;font-weight:700;font-size:22px;color:var(--white);text-transform:uppercase}
.quick-form p{font-size:9.5px;line-height:15px;color:var(--white);margin-top:6px}
.field{background:var(--white);height:32px;margin-top:5px;font-size:9.5px;color:#666;padding:9px 10px}
.field.first{margin-top:12px}
.field.message{height:64px}
.form-btn{margin-top:10px;width:122px;height:32px;background:#111;color:var(--white);font-family:"Raleway",sans-serif;font-weight:700;font-size:11px;display:flex;align-items:center;justify-content:center;gap:5px;text-transform:uppercase}

/* about */
.about{left:0;top:632px;width:1200px;height:400px;background:var(--light)}
.about-title{left:161px;top:694px;font-size:24px}
.about-copy{left:161px;top:740px;width:440px}
.about-photo{left:629px;top:703px;width:408px;height:249px;background:linear-gradient(180deg,#cfd0cf 0%,#e6e5e1 45%,#b7b2a9 100%)}

/* statement band */
.statement{left:0;top:1032px;width:1200px;height:333px;background:linear-gradient(120deg,#2b2420 0%,#4a3a30 40%,#3a2e26 70%,#1f1a17 100%)}
.statement p{position:absolute;left:0;top:112px;width:1200px;text-align:center;font-family:"Raleway",sans-serif;font-weight:400;font-size:32px;line-height:47px;color:var(--white)}

/* services */
.services-title{left:0;top:1408px;width:1200px;text-align:center;font-size:25px}
.service-photo{top:1472px;width:272px;height:198px}
.service-bar{top:1670px;width:272px;height:5px;background:var(--red)}
.service-name{top:1697px;font-size:18px;font-weight:600}
.service-copy{top:1730px;width:272px}
.service-btn{top:1829px;width:111px;height:38px}

/* testimonial */
.testimonial{left:0;top:1923px;width:1200px;height:366px;background:linear-gradient(135deg,var(--red) 0%,var(--red-deep) 100%)}
.testimonial-title{left:0;top:1978px;width:1200px;text-align:center;font-size:25px;color:var(--white)}
.avatar-ring{left:266px;top:2061px;width:130px;height:130px;border-radius:50%;background:#f26a6f;padding:5px}
.avatar{width:120px;height:120px;border-radius:50%;background:linear-gradient(160deg,#a0704e 0%,#d9ad8c 55%,#f1d9c5 100%)}
.quote{left:416px;top:2049px;width:576px;font-style:italic;font-size:12.5px;line-height:24px;color:#fde6e6}
.quote-mark{font-family:Georgia,serif;font-style:normal;font-weight:700;font-size:24px;color:var(--white);line-height:0}
.quote-author{left:422px;top:2186px;font-family:"Open Sans",sans-serif;font-weight:600;font-size:15px;color:var(--white)}
.round-arrow{width:32px;height:32px;border-radius:50%;background:rgba(255,255,255,.25);display:flex;align-items:center;justify-content:center}

/* contact */
.contact{left:0;top:2289px;width:1200px;height:333px;background:#f3f3f3}
.map{left:555px;top:2289px;width:645px;height:333px;background:linear-gradient(90deg,#f3f3f3 0%,#dcdcdc 22%,#d0d0d0 60%,#c8c8c8 100%)}
.contact-title{left:161px;top:2331px;font-family:"Raleway",sans-serif;font-weight:700;font-size:21px;color:var(--ink)}
.contact-row{left:161px;display:flex;align-items:flex-start;gap:14px;font-size:11.5px;line-height:21px;color:#333}
.contact-icon{width:29px;height:29px;border-radius:50%;background:var(--red);display:flex;align-items:center;justify-content:center;flex:none}
.license-title{left:161px;top:2509px;font-family:"Raleway",sans-serif;font-weight:600;font-size:17px;color:#333}
.license{left:161px;font-weight:700;font-size:12.5px;color:#222}

/* footer */
.footer{left:0;top:2622px;width:1200px;height:151px;background:var(--black)}
.footer-nav{left:0;top:2653px;width:1200px;display:flex;justify-content:center;gap:28px;font-family:"Raleway",sans-serif;font-weight:600;font-size:12px;color:var(--white);text-transform:uppercase}
.copyright{left:0;top:2684px;width:1200px;text-align:center;font-size:10.5px;color:#ddd}
.social{left:0;top:2719px;width:1200px;display:flex;justify-content:center;gap:7px}
.social span{width:27px;height:27px;border-radius:50%;border:1.5px solid #ddd}
</style>
</head>
<body>

<div class="abs top-rule"></div>
<header class="abs header"></header>
<div class="abs brand"><span class="brand-dot"></span><span class="brand-name">Kestrel<br>Rendering</span></div>
<div class="abs call">
  <svg width="16" height="16" viewBox="0 0 24 24"><path fill="#e5202a" d="M6.6 10.8c1.4 2.8 3.8 5.1 6.6 6.6l2.2-2.2c.3-.3.7-.4 1-.2 1.1.4 2.3.6 3.6.6.6 0 1 .4 1 1V20c0 .6-.4 1-1 1C10.6 21 3 13.4 3 4c0-.6.4-1 1-1h3.5c.6 0 1 .4 1 1 0 1.3.2 2.5.6 3.6.1.3 0 .7-.2 1z"/></svg>
  Call Us: 555-201-4417
</div>
<nav>
  <span class="abs nav active" style="left:499px">Home</span>
  <span class="abs nav" style="left:573px">Services</span>
  <span class="abs nav" style="left:666px">Portfolio</span>
  <span class="abs nav" style="left:771px">About Us</span>
  <span class="abs nav" style="left:869px">News</span>
  <span class="abs nav" style="left:943px">Contact</span>
  <svg class="abs" style="left:1026px;top:63px" width="12" height="12" viewBox="0 0 24 24"><circle cx="10" cy="10" r="6.5" fill="none" stroke="#222" stroke-width="3"/><path d="M15 15l6 6" stroke="#222" stroke-width="3"/></svg>
</nav>

<section class="abs hero" role="img" aria-label="Plasterer on a ladder finishing a ceiling inside a bright building"></section>
<h1 class="abs hero-title"><span class="first">Kestrel</span><br><span class="second">Rendering</span></h1>
<div class="abs slide-arrow" style="left:36px;top:347px"><svg width="10" height="10" viewBox="0 0 10 10"><path d="M6.5 1L2.5 5l4 4" fill="none" stroke="#fff" stroke-width="1.5"/></svg></div>
<div class="abs slide-arrow" style="left:1145px;top:347px"><svg width="10" height="10" viewBox="0 0 10 10"><path d="M3.5 1l4 4-4 4" fill="none" stroke="#fff" stroke-width="1.5"/></svg></div>

<form class="abs quick-form">
  <h2>Quick Contact Form</h2>
  <p>Sed ut perspiciatis unde omnis iste natus error sit volu ptatem accusantium doloremque laudantium.</p>
  <div class="field first">Name:</div>
  <div class="field">Email:</div>
  <div class="field">Phone:</div>
  <div class="field message">Message:</div>
  <div class="form-btn">Contact Us
    <svg width="10" height="10" viewBox="0 0 10 10"><circle cx="5" cy="5" r="5" fill="#fff"/><path d="M4 2.8L6.2 5 4 7.2" fill="none" stroke="#111" stroke-width="1.4"/></svg>
  </div>
</form>

<section class="abs about"></section>
<h2 class="abs heading about-title">About Kestrel Rendering</h2>
<p class="abs body-copy about-copy">Sed ut perspiciatis unde omnis iste natus sitolu ptatem accusantium doloremque lantium, totme maperiam, eaque ipsa quae ab illo inventore veritati quasi archite ed ut perspiciatis unde omnis iste natus sitolu ptatem accusantium doloremque laudant ium,totmem aperi amaque ipsa quae ab illo inventore veritati quasiar hit ectersplciatis unde omnis iste natus sitolu,maque ipsa quae ab illo inventoretotme maperiam, eaque ipsa quae ab illo invntore veritati quasi archite ed ut perspiciatis unde omnis iste natus sitolu ptatem accusantium doloremque laudant ium,totmem aperi amaque isaua.</p>
<div class="btn" style="left:161px;top:913px;width:111px;height:38px">Read More</div>
<div class="abs about-photo" role="img" aria-label="Modern kitchen with rendered grey wall, island bench and wooden stools"></div>

<section class="abs statement" role="img" aria-label="Close-up of a gloved hand laying bricks with mortar">
  <p>Our years of experience and team of professionals<br>guarantee that Kestrel Rendering will deliver.</p>
</section>

<h2 class="abs heading services-title">What We Do</h2>

<div class="abs service-photo" style="left:161px;background:linear-gradient(160deg,#e8e6e2 0%,#c9c5bf 60%,#a9a49c 100%)" role="img" aria-label="Gloved hand spreading render with a trowel"></div>
<div class="abs service-bar" style="left:161px"></div>
<h3 class="abs heading service-name" style="left:161px">Residential</h3>
<p class="abs body-copy service-copy" style="left:161px">Sed ut perspiciatis unde omnis iste natuslor sitolu ptatem accusantium doloremque laudantium, totm e maperiam, eaque ipsa quaeilloed ut perspiciatis unde omnis iste natus sitolu ptatem.</p>
<div class="btn service-btn" style="left:161px">Read More</div>

<div class="abs service-photo" style="left:464px;background:linear-gradient(180deg,#e9eaea 0%,#cfd1d2 55%,#4a4c4e 100%)" role="img" aria-label="Office reception with smooth white rendered walls"></div>
<div class="abs service-bar" style="left:464px"></div>
<h3 class="abs heading service-name" style="left:464px">Rendering</h3>
<p class="abs body-copy service-copy" style="left:464px">Sed ut perspiciatis unde omnis iste natuslor sitolu ptatem accusantium doloremque laudantium, totm e maperiam, eaque ipsa quaeilloed ut perspiciatis unde omnis iste natus sitolu ptatem .</p>
<div class="btn service-btn" style="left:464px">Read More</div>

<div class="abs service-photo" style="left:765px;background:linear-gradient(180deg,#f2f1ee 0%,#ddd6cc 55%,#a57d56 100%)" role="img" aria-label="Empty commercial interior with ladders and timber floor"></div>
<div class="abs service-bar" style="left:765px"></div>
<h3 class="abs heading service-name" style="left:765px">Commercial</h3>
<p class="abs body-copy service-copy" style="left:765px">Sed ut perspiciatis unde omnis iste natuslor sitolu ptatem accusantium doloremque laudantium, totm e maperiam, eaque ipsa quaeilloed ut perspiciatis unde omnis iste natus sitolu ptatem .</p>
<div class="btn service-btn" style="left:765px">Read More</div>

<section class="abs testimonial"></section>
<h2 class="abs heading testimonial-title">Testimonial</h2>
<div class="abs round-arrow" style="left:177px;top:2096px"><svg width="10" height="10" viewBox="0 0 10 10"><path d="M6.5 1L2.5 5l4 4" fill="none" stroke="#fff" stroke-width="1.5"/></svg></div>
<div class="abs round-arrow" style="left:990px;top:2096px"><svg width="10" height="10" viewBox="0 0 10 10"><path d="M3.5 1l4 4-4 4" fill="none" stroke="#fff" stroke-width="1.5"/></svg></div>
<div class="abs avatar-ring"><div class="avatar" role="img" aria-label="Portrait photo of the client"></div></div>
<blockquote class="abs quote"><span class="quote-mark">&ldquo;</span> Sed ut perspiciatis unde omnis iste natus error sit voluptatem accusantium doloremque lo udantium, totam rem aperiam, eaque ipsa quae ab illo inventore veritatis et quasiarl architecto beatae vitae dicta sunt explicabo.Nemo enim ipsam voluptatem quia voluptas sit aspernatured ut perspiciatis unde omnis iste natus error sit voluptatem accusantium doloremque laudantium, totam rem aperiam, eaque ipsa quae ab illo inventore veritatis et quasi architec <span class="quote-mark">&rdquo;</span></blockquote>
<div class="abs quote-author">Mara Ellis, Harbour Line Logistics</div>

<section class="abs contact"></section>
<div class="abs map" role="img" aria-label="Street map of the service area with a location pin"></div>
<svg class="abs" style="left:726px;top:2449px" width="28" height="34" viewBox="0 0 28 34"><path d="M14 0C6.3 0 0 6.1 0 13.6 0 23.8 14 34 14 34s14-10.2 14-20.4C28 6.1 21.7 0 14 0z" fill="#e5202a"/><circle cx="14" cy="13" r="5" fill="#fff"/></svg>
<h2 class="abs contact-title">Contact Information</h2>
<div class="abs contact-row" style="top:2370px">
  <span class="contact-icon"><svg width="12" height="14" viewBox="0 0 12 14"><path d="M6 0C2.7 0 0 2.6 0 5.8 0 10 6 14 6 14s6-4 6-8.2C12 2.6 9.3 0 6 0z" fill="#fff"/><circle cx="6" cy="5.6" r="2" fill="#e5202a"/></svg></span>
  <span>Kestrel Rendering 1408 Marlow Lane<br>Unit 12, Westbrook</span>
</div>
<div class="abs contact-row" style="top:2421px">
  <span class="contact-icon"><svg width="13" height="13" viewBox="0 0 24 24"><path fill="#fff" d="M6.6 10.8c1.4 2.8 3.8 5.1 6.6 6.6l2.2-2.2c.3-.3.7-.4 1-.2 1.1.4 2.3.6 3.6.6.6 0 1 .4 1 1V20c0 .6-.4 1-1 1C10.6 21 3 13.4 3 4c0-.6.4-1 1-1h3.5c.6 0 1 .4 1 1 0 1.3.2 2.5.6 3.6.1.3 0 .7-.2 1z"/></svg></span>
  <span style="padding-top:4px">T: +31 (0)65 000 4128</span>
</div>
<div class="abs contact-row" style="top:2458px">
  <span class="contact-icon"><svg width="13" height="10" viewBox="0 0 13 10"><rect width="13" height="10" rx="1" fill="#fff"/><path d="M0.5 0.8L6.5 5.5 12.5 0.8" fill="none" stroke="#e5202a" stroke-width="1.3"/></svg></span>
  <span style="padding-top:4px">E: info@kestrelrendering.com</span>
</div>
<h3 class="abs license-title">License Numbers</h3>
<div class="abs license" style="top:2548px">LIC: 400 2193K 561 30847</div>
<div class="abs license" style="top:2572px">LIC: 400 72PL 3906 15824</div>

<footer class="abs footer"></footer>
<nav class="abs footer-nav"><span>Home</span><span>Services</span><span>Products</span><span>Portfolio</span><span>About Us</span><span>Contact</span></nav>
<p class="abs copyright">© 2017 Kestrel Rendering. All Rights Reserved | Legal and Privacy Statement</p>
<div class="abs social"><span></span><span></span><span></span><span></span><span></span></div>

</body>
</html>
```